Perky professional Bookkeeping Business card design needed

I need a business card for my new bookkeeping business. My target market is the owners of small businesses. I am a bright and bubbly young lady, not your typical accountant type and am looking for a bright, modern, perky yet professional card to reflect this.
I would like to use the symbol from framevault http://www.framevault.com/cat.mhtml?searchterm=business+wizard&search_group=&lang=en&search_source=search_form#id=60384915
as my logo but am open to colour schemes.
I want the design of the card to create confidence but not be too formal. Most people are scared of their bookkeepers/accountants and I want to be seen as approachable.
Target Market(s)
Business owners
Industry/Entity Type
Business
Contact Information for Business Card
Tally Spark Bookkeeping - image and name
Maren Holloway BBUS
Registered BAS AGENT 51730628
PO Box 738
Wattle Cove VIC 3958
Ph: 0437682915
Email: maren@tallysparkbookkeeping.com.au
Web: www.tallysparkbookkeeping.com.au
Tag line: Acheiving Maximum Results (not sure whether to include)
Look and feel

```html
<!DOCTYPE html>
<html lang="en">
<head>
<meta charset="utf-8">
<title>Tally Spark Bookkeeping – Business Card</title>
<link rel="stylesheet" href="https://fonts.googleapis.com/css2?family=Cabin:wght@400;500&display=swap">
<style>
  :root {
    --backdrop: #ece6de;
    --card-top: #faf1e4;
    --card-bottom: #f6c67c;
    --orange: #e5782a;
    --orange-light: #f2a14a;
    --peach-band: #eba06c;
    --peach-tab: #f3c49a;
    --ink: #5a2812;
  }
  html, body {
    margin: 0;
    width: 1200px;
    height: 900px;
    overflow: hidden;
    background: var(--backdrop);
    font-family: "Cabin", "Trebuchet MS", sans-serif;
    color: var(--ink);
  }
  .card {
    position: absolute;
    width: 520px;
    height: 300px;
    background: linear-gradient(180deg, var(--card-top) 0%, var(--card-bottom) 100%);
    box-shadow: 0 6px 18px rgba(60, 35, 10, 0.25);
    overflow: hidden;
  }
  .card svg { position: absolute; inset: 0; }
  .card--front { left: 70px; top: 130px; }
  .card--back { left: 610px; top: 470px; }

  .brand {
    position: absolute;
    left: 205px;
    top: 100px;
    display: flex;
    align-items: center;
    gap: 14px;
  }
  .brand__dot {
    width: 76px;
    height: 76px;
    border-radius: 50%;
    background: var(--orange);
  }
  .brand__name {
    font-weight: 500;
    color: var(--ink);
    line-height: 1.05;
  }
  .brand__name-main { display: block; font-size: 30px; letter-spacing: 0.5px; }
  .brand__name-sub { display: block; font-size: 22px; }

  .holder {
    position: absolute;
    left: 112px;
    top: 62px;
  }
  .holder__name { font-size: 24px; font-weight: 500; margin: 0; }
  .holder__title { font-size: 12px; margin: 4px 0 0; }

  .contact {
    position: absolute;
    left: 112px;
    top: 150px;
    font-size: 12px;
    line-height: 1.35;
  }
  .contact p { margin: 0; }

  .website {
    position: absolute;
    left: 140px;
    top: 252px;
    font-size: 13px;
    font-weight: 500;
  }
</style>
</head>
<body>

<section class="card card--front" aria-label="Card front">
  <svg viewBox="0 0 520 300" width="520" height="300" aria-hidden="true">
    <path class="swoosh-fill" d="M0,220 C40,280 120,292 210,290 L520,262 L520,300 L0,300 Z" fill="var(--orange-light)" opacity="0.55"/>
    <path d="M45,40 C-5,160 40,285 210,290 L520,262" fill="none" stroke="var(--orange-light)" stroke-width="16"/>
    <path d="M72,30 C22,140 52,252 200,262 L520,234" fill="none" stroke="var(--orange)" stroke-width="12"/>
  </svg>
  <div class="brand">
    <span class="brand__dot"></span>
    <span class="brand__name">
      <span class="brand__name-main">TALLY SPARK</span>
      <span class="brand__name-sub">Bookkeeping</span>
    </span>
  </div>
</section>

<section class="card card--back" aria-label="Card back">
  <svg viewBox="0 0 520 300" width="520" height="300" aria-hidden="true">
    <rect x="100" y="82" width="420" height="62" fill="var(--peach-band)"/>
    <rect x="100" y="52" width="200" height="36" fill="var(--peach-tab)"/>
    <rect x="0" y="228" width="520" height="10" fill="var(--orange)"/>
    <rect x="0" y="238" width="520" height="40" fill="var(--peach-tab)" opacity="0.6"/>
    <rect x="0" y="278" width="520" height="12" fill="var(--orange)"/>
  </svg>
  <div class="holder">
    <h1 class="holder__name">Maren Holloway</h1>
    <p class="holder__title">BBUS Registered BAS AGENT 51730628</p>
  </div>
  <div class="contact">
    <p>PO Box 738 Wattle Cove VIC 3958</p>
    <p>Ph: 0437682915</p>
    <p>maren@tallysparkbookkeeping.com.au</p>
  </div>
  <div class="website">www.tallysparkbookkeeping.com.au</div>
</section>

</body>
</html>
```